New Business Card for Casual Beachfront Cafe

Quirky Beachfront Cafe at Moana, South Australia needs a DOUBLE SIDED business card to print on PrintHollow.

Target Market(s)

Business Cards sit on the counter for Guests to take with them. Please view our website www.saltkettlecafe.com.au to get a feel for the Cafe. You may also view our Instagram at @saltkettlecafe

Industry/Entity Type

Cafe / Restaurant

Contact Information for Business Card

Information equivalent to: Breakfast, Lunch, Dinner, Coffee, Takeaway / 918 Marlin Road Moana SA 5169 / Menu & Opening Hours: www.saltkettlecafe.com.au / ph (08) 7194 2618

Requirements
Must have
• Information equivalent to: Breakfast, Lunch, Dinner, Coffee, Takeaway / 918 Marlin Road Moana SA 5169 / Menu & Opening Hours: www.saltkettlecafe.com.au / ph (08) 7194 2618
Nice to have
• Potentially some of our trademark colours (Cafe can be searched via Google)
Should not have
• Must NOT have image of the building. May have the logo provided on one side but not necessarily, depending on how you wish to design the card

```html
<!DOCTYPE html>
<html lang="en">
<head>
<meta charset="utf-8">
<title>Salt Kettle Cafe – Business Card</title>
<link rel="stylesheet" href="https://fonts.googleapis.com/css2?family=Montserrat:wght@400;600;800&display=swap">
<style>
  :root {
    --bg: #8a8a88;
    --card-white: #ffffff;
    --navy: #1b3f8f;
    --blue: #1f4f9a;
    --blue-dark: #1a4489;
    --blue-light: #2a5ca8;
    --yellow: #f7e400;
    --grey-text: #555a60;
    --orange: #c8622a;
  }
  * { box-sizing: border-box; margin: 0; padding: 0; }
  html, body { width: 1200px; height: 801px; overflow: hidden; }
  body {
    background: var(--bg);
    font-family: "Montserrat", sans-serif;
    display: flex;
    align-items: center;
    justify-content: center;
    gap: 40px;
  }
  .card {
    width: 520px;
    height: 317px;
    position: relative;
    overflow: hidden;
    box-shadow: 0 6px 18px rgba(0,0,0,0.25);
  }
  /* Front */
  .card-front { background: var(--card-white); }
  .front-name {
    position: absolute;
    left: 34px;
    top: 118px;
    width: 190px;
    color: var(--navy);
    font-weight: 800;
    font-size: 30px;
    line-height: 1.05;
    text-transform: uppercase;
    text-align: center;
  }
  .divider {
    position: absolute;
    left: 246px;
    top: 92px;
    width: 1px;
    height: 112px;
    background: var(--navy);
    opacity: 0.7;
  }
  .contact {
    position: absolute;
    left: 264px;
    top: 96px;
    list-style: none;
    font-size: 13px;
    color: var(--grey-text);
    line-height: 1.75;
  }
  .contact li { display: flex; align-items: center; gap: 6px; }
  .contact svg { width: 11px; height: 11px; fill: var(--navy); flex: none; }
  .contact .hours { color: var(--navy); font-weight: 600; margin-top: 6px; }
  .services {
    position: absolute;
    left: 0; right: 0;
    bottom: 34px;
    text-align: center;
    font-size: 15px;
    letter-spacing: 0.04em;
    color: var(--grey-text);
  }
  .services .dot { color: var(--orange); margin: 0 8px; }
  /* Back */
  .card-back { background: var(--blue); }
  .back-pattern {
    position: absolute;
    inset: 0;
    background: linear-gradient(135deg, var(--blue-dark) 0%, var(--blue) 55%, var(--blue-light) 100%);
  }
  .back-name {
    position: absolute;
    inset: 0;
    display: flex;
    align-items: center;
    justify-content: center;
    text-align: center;
    color: var(--yellow);
    font-weight: 800;
    font-size: 38px;
    line-height: 1.05;
    text-transform: uppercase;
  }
</style>
</head>
<body>
  <section class="card card-front" aria-label="Card front">
    <p class="front-name">Salt Kettle Cafe</p>
    <div class="divider"></div>
    <ul class="contact">
      <li>
        <svg viewBox="0 0 24 24" aria-hidden="true"><path d="M6.6 10.8a15 15 0 0 0 6.6 6.6l2.2-2.2a1 1 0 0 1 1-.25 11.4 11.4 0 0 0 3.6.57 1 1 0 0 1 1 1V20a1 1 0 0 1-1 1A17 17 0 0 1 3 4a1 1 0 0 1 1-1h3.5a1 1 0 0 1 1 1c0 1.25.2 2.45.57 3.57a1 1 0 0 1-.25 1z"/></svg>
        (08) 7194 2618
      </li>
      <li>
        <svg viewBox="0 0 24 24" aria-hidden="true"><path d="M12 2a7 7 0 0 0-7 7c0 5.25 7 13 7 13s7-7.75 7-13a7 7 0 0 0-7-7zm0 9.5A2.5 2.5 0 1 1 12 6.5a2.5 2.5 0 0 1 0 5z"/></svg>
        918 Marlin Road Moana SA 5169
      </li>
      <li class="hours">Opening Hours:</li>
      <li>www.saltkettlecafe.com.au</li>
    </ul>
    <p class="services">
      Breakfast<span class="dot">•</span>Lunch<span class="dot">•</span>Dinner<span class="dot">•</span>Coffee<span class="dot">•</span>Takeaway
    </p>
  </section>

  <section class="card card-back" aria-label="Card back">
    <div class="back-pattern" role="img" aria-label="Tone-on-tone repeating cafe name pattern across the blue background"></div>
    <p class="back-name">Salt Kettle<br>Cafe</p>
  </section>
</body>
</html>
```